lark to lead - dorian whitcombe personal speaking/consulting website

custom website for my personal speaking/consulting services brand, you can see the basic site we are using as a placeholder at www.larktolead.example now. I want to re-position this to more of a personal brand site and have video samples of speaking events, downloadable content, a video blog, and links to podcast. I really like the design of marcoveldin.example and the feature set should be fairly similar to his. I'll begin to compile more stock images etc. to use for sliders like he has done, for now we'll need to use stock imagery or existing photography from my social accounts. You can get a feel for social at all platforms/dwhitrealty i.e. facebook.com/dwhitrealty. the site should be primarily geared toward showcasing speaking/consulting services and content, as well as be flexible to allow for additional downloadables etc. in the future.

Target Market(s)

entrepreneurs and leaders looking to grow themselves, their business, and those they lead.

Coding

Coded - Design and coding required

Number of Pages Required

3 page

Font styles to use
Sans Serif

Colors

Designer to choose colors to be used in the design.

Requirements
Must have
• modern slick design, video blog, podcast feed, registration for people to subscribe to newsletter

```html
<!DOCTYPE html>
<html lang="en">
<head>
<meta charset="utf-8">
<title>Lark to Lead — Dorian Whitcombe</title>
<link rel="stylesheet" href="https://fonts.googleapis.com/css2?family=Cinzel:wght@600;700&family=Open+Sans:wght@400;600;700&display=swap">
<style>
:root{
  --orange:#f26a2e;
  --orange-light:#f7934f;
  --peach:#fdece3;
  --ink:#222222;
  --grey:#6f6f6f;
  --dark:#121212;
  --footer-bar:#1b1b1b;
  --white:#ffffff;
}
*{margin:0;padding:0;box-sizing:border-box}
html,body{width:1200px;height:3632px;overflow:hidden}
body{position:relative;background:var(--white);font-family:"Open Sans",Arial,sans-serif;color:var(--ink)}
.abs{position:absolute}
.serif{font-family:"Cinzel",Georgia,serif;font-weight:700}

/* nav */
.site-nav{left:0;top:0;width:1200px;height:72px;background:var(--white);z-index:5}
.brand{left:72px;top:18px;font-size:26px;font-weight:700;color:var(--ink)}
.nav-links{right:72px;top:27px;display:flex;gap:30px;list-style:none;font-size:12px;letter-spacing:1px;text-transform:uppercase;color:var(--ink)}
.nav-links .active{color:var(--orange)}

/* hero */
.hero{left:0;top:72px;width:1200px;height:568px;background:linear-gradient(180deg,#9fb9cf 0%,#c9d3d8 30%,#a7764a 55%,#7a5a3c 70%,#3f5565 85%,#2c3a44 100%)}
.hero-portrait{left:700px;top:72px;width:500px;height:568px;background:radial-gradient(ellipse at 55% 40%,#d9a98e 0%,#a77a62 30%,#3b4656 60%,rgba(40,50,62,0) 80%)}
.hero-title{left:180px;top:210px;font-size:54px;line-height:1.25;color:var(--white);letter-spacing:1px}

/* welcome */
.welcome-title{left:72px;top:740px;font-size:32px}
.welcome-text{left:72px;top:800px;width:520px;font-size:14px;line-height:1.8;color:var(--grey)}
.welcome-text p+p{margin-top:18px}
.btn{display:flex;align-items:center;justify-content:center;border-radius:30px;font-size:13px;font-weight:600;letter-spacing:1px;text-transform:uppercase}
.btn-orange{background:var(--orange);color:var(--white)}
.btn-white{background:var(--white);color:var(--orange)}
.welcome-btn{left:72px;top:1060px;width:190px;height:50px}
.welcome-frame{left:745px;top:700px;width:370px;height:420px;border:2px solid var(--orange)}
.welcome-square{left:690px;top:1000px;width:140px;height:140px;background:#eeeeee}
.welcome-photo{left:700px;top:740px;width:390px;height:400px;background:radial-gradient(ellipse at 50% 45%,#d7a88c 0%,#a9806a 25%,#34404f 55%,#8fb0c8 80%)}

/* podcast */
.section-title{left:0;width:1200px;text-align:center;font-size:32px}
.podcast-title{top:1240px}
.podcast-tile{top:1330px;width:300px;height:370px}
.podcast-tile span{position:absolute;left:0;bottom:36px;width:100%;text-align:center;font-size:16px;color:var(--white)}
.tile-1{left:0;background:linear-gradient(135deg,#c9b39c,#8c7a69)}
.tile-2{left:300px;background:linear-gradient(135deg,#9aa0a8,#3f4753)}
.tile-3{left:600px;background:linear-gradient(135deg,#b28e85,#5e4b4a)}
.tile-4{left:900px;background:linear-gradient(135deg,#8f7b72,#3b3232)}

/* downloads */
.downloads{left:0;top:1700px;width:1200px;height:560px;background:var(--peach)}
.downloads-wave{left:0;top:1700px}
.downloads-title{left:72px;top:1800px;font-size:30px}
.downloads-lead{left:72px;top:1862px;font-size:15px;color:var(--grey)}
.downloads-sub{left:72px;top:1900px;font-size:22px}
.downloads-note{left:72px;top:1950px;font-size:14px;color:var(--orange)}
.downloads-btn{left:72px;top:2120px;width:190px;height:50px}
.laptop-lid{left:680px;top:1920px;width:500px;height:250px;background:#2a2a2a;border-radius:14px 14px 0 0;padding:14px}
.laptop-screen{width:100%;height:100%;background:linear-gradient(120deg,#d7d3cc 0%,#c9c2b6 45%,#28313d 60%,#d2cdc3 80%)}
.laptop-caption{left:715px;top:2136px;font-size:11px;color:var(--white);background:rgba(0,0,0,.55);padding:2px 8px}
.laptop-base{left:630px;top:2170px;width:570px;height:18px;background:linear-gradient(180deg,#d9d9d9,#9e9e9e);border-radius:0 0 18px 18px}

/* events */
.events-title{top:2330px}
.event-card{top:2400px;width:312px}
.event-photo{height:220px}
.event-date{position:absolute;left:0;top:160px;width:60px;height:70px;background:var(--orange);color:var(--white);text-align:center;font-size:11px;padding-top:10px}
.event-date b{display:block;font-size:22px}
.event-text{margin-top:26px;font-size:13px;line-height:1.7;color:var(--grey)}
.card-1{left:72px}.card-1 .event-photo{background:linear-gradient(135deg,#b4462f,#3a2522)}
.card-2{left:444px}.card-2 .event-photo{background:linear-gradient(135deg,#d9d6d2,#5b5a5f)}
.card-3{left:816px}.card-3 .event-photo{background:linear-gradient(135deg,#e8e6e2,#8f8a86)}

/* footer */
.footer-bg{left:0;top:3040px;width:1200px;height:540px;background:linear-gradient(160deg,var(--orange) 0%,var(--orange-light) 100%)}
.signup{left:72px;top:2780px;width:1056px;height:345px;background:var(--dark)}
.signup-title{left:72px;top:2825px;width:1056px;text-align:center;font-size:28px;color:var(--white)}
.field{border:1px solid #cfcfcf;border-radius:22px;color:var(--white);font-size:13px;padding:11px 22px}
.field-name{left:260px;top:2900px;width:330px;height:42px}
.field-email{left:260px;top:2955px;width:330px;height:42px}
.field-phone{left:260px;top:3010px;width:330px;height:42px}
.field-message{left:620px;top:2900px;width:320px;height:152px;border-radius:18px}
.signup-btn{left:500px;top:3100px;width:200px;height:50px}
.footer-brand{left:0;top:3270px;width:1200px;text-align:center;font-size:40px;font-weight:700;color:var(--white)}
.social{left:390px;top:3396px;display:flex;gap:22px}
.social i{display:block;width:50px;height:50px;border-radius:50%;background:rgba(255,255,255,.22)}
.social i.on{background:#111}
.footer-links{left:0;top:3490px;width:1200px;display:flex;justify-content:center;gap:56px;list-style:none;font-size:13px;color:var(--white)}
.footer-bar{left:0;top:3580px;width:1200px;height:52px;background:var(--footer-bar);color:var(--white);font-size:12px;display:flex;align-items:center;justify-content:center}
</style>
</head>
<body>

<header class="abs site-nav">
  <div class="abs brand">Lark to Lead</div>
  <ul class="abs nav-links">
    <li class="active">Home</li><li>About</li><li>Video Blog</li><li>Podcast</li><li>Events</li><li>Contact</li>
  </ul>
</header>

<section>
  <div class="abs hero" role="img" aria-label="Autumn lakeside landscape with mountains"></div>
  <div class="abs hero-portrait" role="img" aria-label="Portrait of Dorian Whitcombe smiling"></div>
  <h1 class="abs serif hero-title">LOREM IPSUM IS<br>SIMPLY DUMMY TEXT.</h1>
</section>

<section>
  <h2 class="abs serif welcome-title">WELCOME TO LARK TO LEAD</h2>
  <div class="abs welcome-text">
    <p>Lorem Ipsum is simply dummy text of the printing and typesetting industry. Lorem Ipsum has been the industry's standard dummy text ever.</p>
    <p>It has survived not only five centuries, but also the leap into electronic typesetting, remaining essentially unchanged. It was popularised in the 1960s with the release of sheets containing Lorem Ipsum passages, and more recently with desktop publishing software including versions of Lorem Ipsum.</p>
  </div>
  <div class="abs btn btn-orange welcome-btn">Read More</div>
  <div class="abs welcome-square"></div>
  <div class="abs welcome-frame"></div>
  <div class="abs welcome-photo" role="img" aria-label="Portrait of Dorian Whitcombe outdoors"></div>
</section>

<section>
  <h2 class="abs serif section-title podcast-title">FEATURED PODCAST</h2>
  <div class="abs podcast-tile tile-1" role="img" aria-label="Podcast episode photo: friends laughing"><span>Lorem Ipsum is simply dummy</span></div>
  <div class="abs podcast-tile tile-2" role="img" aria-label="Podcast episode photo: mascot character"><span>Lorem Ipsum is simply dummy</span></div>
  <div class="abs podcast-tile tile-3" role="img" aria-label="Podcast episode photo: runner training"><span>Lorem Ipsum is simply dummy</span></div>
  <div class="abs podcast-tile tile-4" role="img" aria-label="Podcast episode photo: celebrating at sunset"><span>Lorem Ipsum is simply dummy</span></div>
</section>

<section>
  <div class="abs downloads"></div>
  <svg class="abs downloads-wave" width="1200" height="560" viewBox="0 0 1200 560" aria-hidden="true">
    <path d="M0 430 C300 420 700 330 1200 250 L1200 560 L0 560 Z" fill="var(--orange)"/>
  </svg>
  <h2 class="abs serif downloads-title">DOWNLOADABLE CONTENT</h2>
  <p class="abs downloads-lead">Lorem Ipsum is simply dummy text.</p>
  <p class="abs serif downloads-sub">IT HAS SURVIVED NOT ONLY FIVE.</p>
  <p class="abs downloads-note">Lorem Ipsum is simply</p>
  <div class="abs btn btn-white downloads-btn">Explore More</div>
  <div class="abs laptop-lid"><div class="laptop-screen" role="img" aria-label="Video still of Dorian Whitcombe speaking"></div></div>
  <div class="abs laptop-caption">Dorian Whitcombe</div>
  <div class="abs laptop-base"></div>
</section>

<section>
  <h2 class="abs serif section-title events-title">SPEAKING EVENTS</h2>
  <article class="abs event-card card-1">
    <div class="event-photo" role="img" aria-label="Speaker on stage before an audience"></div>
    <div class="event-date">MAY<b>21</b></div>
    <p class="event-text">Lorem Ipsum is simply dummy text of the printing and typesetting industry. Lorem Ipsum has been.</p>
  </article>
  <article class="abs event-card card-2">
    <div class="event-photo" role="img" aria-label="Seminar audience seated in rows"></div>
    <div class="event-date">MAY<b>21</b></div>
    <p class="event-text">Lorem Ipsum is simply dummy text of the printing and typesetting industry. Lorem Ipsum has been.</p>
  </article>
  <article class="abs event-card card-3">
    <div class="event-photo" role="img" aria-label="Workshop presentation in a bright room"></div>
    <div class="event-date">MAY<b>21</b></div>
    <p class="event-text">Lorem Ipsum is simply dummy text of the printing and typesetting industry. Lorem Ipsum has been.</p>
  </article>
</section>

<footer>
  <div class="abs footer-bg"></div>
  <div class="abs signup"></div>
  <h2 class="abs serif signup-title">SPEAKING EVENTS</h2>
  <div class="abs field field-name">Name</div>
  <div class="abs field field-email">Email</div>
  <div class="abs field field-phone">Phone</div>
  <div class="abs field field-message">Message</div>
  <div class="abs btn btn-orange signup-btn">Read More</div>
  <div class="abs footer-brand">Lark to Lead</div>
  <div class="abs social" aria-label="Social links"><i></i><i></i><i class="on"></i><i></i><i></i><i></i></div>
  <ul class="abs footer-links"><li>Home</li><li>About</li><li>Video Blog</li><li>Podcast</li><li>Events</li><li>Contact</li></ul>
  <div class="abs footer-bar">©Lark to Lead 2019 · All Right Reserved</div>
</footer>

</body>
</html>
```